Place holder for book called THE AUDACITY OF DAWN

I'm relying on your imaginative genius because I have no suggestions for you. Attached is a picture of the author when young if it will be of help. The only other info I can offer is that the author uses the alphabet as a theme.

Book info:
Title: THE AUDACITY OF DAWN
Author: ROSALIND MCARDLE

This is a memoir. It's a story of daring to hope when things seem hopeless, of problems when changing countries, of making success of dross. I'm looking for a design that is daring, eye-catching but promises hope. I hope it's not impossible.

Can you give me a place holder for the book to go onto my website and for pre-publicity? Then, in 6-9 months I'll pay another $150 for the completion of hardcover, paperback and ebook covers.

```html
<!DOCTYPE html>
<html lang="en">
<head>
<meta charset="utf-8">
<title>The Audacity of Dawn — Rosalind McArdle</title>
<link rel="stylesheet" href="https://fonts.googleapis.com/css2?family=Josefin+Sans:wght@300;400&family=Great+Vibes&family=Dancing+Script:wght@700&display=swap">
<style>
  :root {
    --page-bg: #ffffff;
    --sun: #fbf7c8;
    --sky-pale: #e9f3cf;
    --sky-blue: #5f8ec4;
    --sky-teal: #8fd0cf;
    --haze: #eef4d6;
    --ground: #3a2f7a;
    --ground-deep: #2a1f63;
    --title-navy: #262a66;
    --title-purple: #8b2a9c;
    --author-white: #ffffff;
  }
  * { margin: 0; padding: 0; box-sizing: border-box; }
  html, body {
    width: 1200px;
    height: 1200px;
    overflow: hidden;
    background: var(--page-bg);
  }
  .canvas {
    position: relative;
    width: 1200px;
    height: 1200px;
  }
  .cover {
    position: absolute;
    left: 245px;
    top: 60px;
    width: 710px;
    height: 1080px;
    overflow: hidden;
  }
  .cover-art {
    position: absolute;
    inset: 0;
    background:
      radial-gradient(circle at 12% 14%, var(--sun) 0%, rgba(251,247,200,0.85) 14%, rgba(251,247,200,0) 42%),
      radial-gradient(ellipse at 60% 62%, var(--haze) 0%, rgba(238,244,214,0) 45%),
      linear-gradient(180deg,
        var(--sky-pale) 0%,
        var(--sky-blue) 24%,
        var(--sky-teal) 46%,
        var(--haze) 62%,
        #9aa8c8 74%,
        var(--ground) 88%,
        var(--ground-deep) 100%);
  }
  .title {
    position: absolute;
    left: 0;
    right: 0;
    top: 150px;
    text-align: center;
    font-family: "Josefin Sans", sans-serif;
    font-weight: 300;
    line-height: 1;
  }
  .title-the {
    display: block;
    font-size: 78px;
    color: var(--title-navy);
    letter-spacing: 4px;
    margin-left: 60px;
  }
  .title-main {
    display: block;
    font-size: 118px;
    color: var(--title-navy);
    letter-spacing: 2px;
    margin-top: 20px;
    margin-left: 40px;
  }
  .title-of {
    display: block;
    font-family: "Great Vibes", cursive;
    font-size: 120px;
    color: var(--title-purple);
    margin-top: -6px;
    margin-left: 20px;
    line-height: 0.9;
  }
  .title-dawn {
    display: block;
    font-size: 212px;
    color: var(--title-purple);
    letter-spacing: 4px;
    margin-top: -30px;
    margin-left: 30px;
  }
  .subtitle {
    position: absolute;
    right: 70px;
    top: 730px;
    font-family: "Dancing Script", cursive;
    font-weight: 700;
    font-size: 30px;
    color: var(--title-navy);
  }
  .author {
    position: absolute;
    left: 0;
    right: 0;
    bottom: 70px;
    text-align: center;
    font-family: "Josefin Sans", sans-serif;
    font-weight: 400;
    color: var(--author-white);
    font-size: 44px;
    letter-spacing: 3px;
    font-variant: small-caps;
  }
  .author .initial { font-size: 62px; }
</style>
</head>
<body>
  <main class="canvas">
    <section class="cover">
      <div class="cover-art" role="img" aria-label="Sunlit sky with soft bokeh fading into a field of grass at dusk, a dandelion seed head and a butterfly"></div>
      <h1 class="title">
        <span class="title-the">THE</span>
        <span class="title-main">AUDACITY</span>
        <span class="title-of">of</span>
        <span class="title-dawn">DAWN</span>
      </h1>
      <p class="subtitle">a memoir</p>
      <p class="author"><span class="initial">R</span>osalind <span class="initial">M</span>c<span class="initial">A</span>rdle</p>
    </section>
  </main>
</body>
</html>
```